Geschäftspapiere für Hundebetreuung
Zielgruppe
Mein Unternehmen richtet sich an Hundehalter, die freudig mit ihrem Hund arbeiten oder trainieren wollen oder eine positiv arbeitende Hundebetreuung oder Gassi-Gänger suchen. Hierbei liegt der Fokus auf Emotionen des Hundes, Emotionen des Hundehalters, Körpersprache und kleinschrittiges Training. Gemeinsames freudiges Training schafft Vertrauen und Bindung und ermöglicht Hund und Halter Freiraum. Ziel des Angebotes ist es, dass Hundehalter Verständnis für die Emotionen und Interessen des Hundes zu entwickeln und das für sich zu nutzen lernen, dem Hund das geben, was er in der jeweiligen Situation braucht und das ganze auf wissenschaftlich fundierter Basis.
Aufgabenstellung
Das Logo muss enthalten sein, ansonsten sind der Kreativität keine Grenzen gesetzt :)
Es sollte nur von Rechnung, über Angebot für alles nutzbar sein.
Das Unternehmen ist ein Einzelunternehmen, sprich der Firmenname ist mein eigener Name 'Sabine Krollmann' und Pfotenfreunde nur Website und Marke.

```html
<!DOCTYPE html>
<html lang="de">
<head>
<meta charset="utf-8">
<title>Pfotenfreunde – Briefpapier</title>
<link href="https://fonts.googleapis.com/css2?family=Lato:wght@400;700&display=swap" rel="stylesheet">
<style>
  :root{
    --backdrop:#e3e4e2;
    --paper:#fbfbf3;
    --ink:#2c2c2c;
    --ink-soft:#555a5f;
    --leaf:#8cc063;
    --slate:#5f6d7c;
    --signature:#9aa0a6;
  }
  *{margin:0;padding:0;box-sizing:border-box}
  html,body{width:1200px;height:803px;overflow:hidden;background:var(--backdrop)}
  body{font-family:"Lato",sans-serif;color:var(--ink);position:relative}
  .letterhead{
    position:absolute;left:331px;top:21px;width:537px;height:761px;
    background:var(--paper);box-shadow:0 2px 10px rgba(0,0,0,.12);
  }
  .brand{
    position:absolute;right:34px;top:52px;display:flex;align-items:center;gap:7px;
    font-size:19px;font-weight:400;color:var(--leaf);letter-spacing:.2px;
  }
  .brand-dot{width:14px;height:14px;border-radius:50%;background:var(--slate)}
  .date{position:absolute;left:41px;top:104px;font-size:8px;color:var(--leaf);opacity:.7}
  .salutation{position:absolute;left:41px;top:145px;font-size:13px;font-weight:700;text-transform:uppercase;letter-spacing:.1px}
  .body-copy{position:absolute;left:41px;top:190px;width:458px;font-size:11.2px;line-height:19.8px;color:var(--ink)}
  .body-copy p + p{margin-top:19.8px}
  .closing{position:absolute;left:41px;top:603px}
  .closing-word{font-size:10.5px;color:var(--leaf)}
  .sender{margin-top:6px;font-size:12.5px;font-weight:700;line-height:20px;text-transform:uppercase}
  .signature{position:absolute;left:392px;top:624px;width:98px;height:34px;border-radius:17px;
    background:linear-gradient(90deg,rgba(154,160,166,.25),rgba(154,160,166,.45))}
  .footer-rule{position:absolute;left:19px;top:692px;width:493px;height:3px}
  .rule-green{position:absolute;left:0;top:0;width:384px;height:3px;background:var(--leaf)}
  .rule-dash{position:absolute;top:0;height:3px;background:var(--slate)}
  .contact{position:absolute;left:32px;top:706px;list-style:none;font-size:7.2px;color:var(--ink-soft)}
  .contact li{display:flex;align-items:center;gap:9px;height:13.5px}
  .contact svg{width:8px;height:8px;fill:none;stroke:var(--leaf);stroke-width:1.4}
  .bank{position:absolute;left:363px;top:706px;font-size:7.2px;color:var(--ink-soft);line-height:15px}
  .bank span{display:inline-block;width:31px}
</style>
</head>
<body>
  <main class="letterhead">
    <div class="brand"><span class="brand-dot"></span>Pfotenfreunde</div>

    <div class="date">23rd September 2022</div>
    <h1 class="salutation">Dear Lena Marwitz,</h1>

    <section class="body-copy">
      <p>Lorem ipsum dolor sit amet, consectetur adipiscing elit, sed do eiusmod tempor incididunt ut labore et dolore magna aliqua. Ut enim ad minim veniam, quis nostrud exercitation ullamco laboris nisi ut aliquip ex ea commodo consequat. Duis aute irure dolor in reprehenderit in.</p>
      <p>Sed ut perspiciatis unde omnis iste natus error sit voluptatem accusantium doloremque laudantium, totam rem aperiam, eaque ipsa quae ab illo inventore veritatis et quasi architecto beatae vitae dicta sunt explicabo. Nemo enim ipsam voluptatem quia voluptas sit aspernatur aut odit aut fugit, sed quia consequuntur magni dolores eos qui ratione voluptatem sequi nesciunt. Neque porro quisquam est, qui dolorem ipsum quia dolor sit amet, consectetur, adipisci velit, sed quia non numquam eius modi tempora incidunt ut labore et dolore magnam aliquam quaerat voluptatem. Ut enim ad minima veniam, quis nostrum exercitationem ullam corporis suscipit laboriosam, nisi ut aliquid ex ea commodi consequatur.</p>
    </section>

    <div class="closing">
      <div class="closing-word">Sincerly,</div>
      <div class="sender">Sabine Krollmann<br>Company CEO &amp; Founder</div>
    </div>
    <div class="signature" role="img" aria-label="Handschriftliche Unterschrift"></div>

    <div class="footer-rule">
      <div class="rule-green"></div>
      <div class="rule-dash" style="left:388px;width:12px"></div>
      <div class="rule-dash" style="left:404px;width:12px"></div>
      <div class="rule-dash" style="left:420px;width:73px"></div>
    </div>

    <ul class="contact">
      <li><svg viewBox="0 0 10 10"><path d="M2 1l2 2-1 1.2a5 5 0 0 0 2.8 2.8L7 6l2 2-1.2 1.2C4.5 9 1 5.5.8 2.2z"/></svg>+49 151 274 830</li>
      <li><svg viewBox="0 0 10 10"><rect x="1" y="1.5" width="8" height="5.5" rx=".6"/><path d="M3.5 9h3M5 7v2"/></svg>www.pfotenfreunde-hund.de</li>
      <li><svg viewBox="0 0 10 10"><rect x="1" y="2" width="8" height="6" rx=".6"/><path d="M1 2.5l4 3 4-3"/></svg>hallo@pfotenfreunde-hund.de</li>
    </ul>

    <div class="bank">
      <div><span>IBAN</span>: DE27 4305 0001 8821 6640</div>
      <div><span>BBAN</span>: 43050 88216</div>
    </div>
  </main>
</body>
</html>
```